4' x 8' Construction Project Sign, think of a very large business card

We need project signs for our construction sites, the sign will be mounted along the road so cars driving by can quickly read. the sign should be able to be read as cars drive by doing highway speed.

Think like your making a large business card

I would like to include "NOW HIRING" Superintendents, Project Managers, Pipe Foremen, Pipe Layers, and Equipment Operators

Description of services we provide should include

Civil Construction Services
Land Clearing
Excavation
Underground Utilities
Environmental Maintenance

The 2 objectives is to market to future clients and to recruit new employees

The sign will be mounted on posts at the entrance of our construction projects

Low design quality

Target Market(s)

Construction and land developers

Industry/Entity Type

Construction Company

Font styles to use
Other font styles liked:
• Hypatia Sans Pro lite

Colors

Designer to choose colors to be used in the design.

Requirements
Must have
• Clean and easy to read
• Civil Construction Services
• Land Clearing
• Excavation
• Underground Utilities
• Road Construction

```html
<!DOCTYPE html>
<html lang="en">
<head>
<meta charset="utf-8">
<title>Harlan Ridge Civil Construction – Project Sign</title>
<link rel="stylesheet" href="https://fonts.googleapis.com/css2?family=Open+Sans:wght@600;800&family=Questrial&family=Titillium+Web:wght@700&display=swap">
<style>
  :root {
    --navy: #223f7c;
    --ink: #1b1b1b;
    --paper: #ffffff;
    --mist: #e6e6e6;
    --steel: #5b5b5d;
    --backdrop: #5e5e5e;
  }
  * { margin: 0; padding: 0; box-sizing: border-box; }
  html, body { width: 1200px; height: 701px; overflow: hidden; background: var(--backdrop); }
  .sign {
    position: absolute; left: 0; top: 50px;
    width: 1200px; height: 600px; overflow: hidden;
  }
  .sign-shapes { position: absolute; inset: 0; width: 100%; height: 100%; }
  .hiring-title {
    position: absolute; left: 66px; top: 48px;
    font: 800 101px/94px "Open Sans", sans-serif;
    color: var(--paper); letter-spacing: -1px;
  }
  .role-list, .service-list { position: absolute; list-style: none; }
  .role-list { left: 83px; top: 308px; }
  .role-list li {
    display: flex; align-items: center; height: 52px;
    font: 600 36px "Open Sans", sans-serif; color: var(--paper);
  }
  .role-list .tick { width: 30px; height: 30px; margin-right: 24px; flex: none; }
  .service-list { left: 709px; top: 316px; }
  .service-list li {
    display: flex; align-items: center; height: 42px; margin-bottom: 0.5px;
    font: 29px "Questrial", sans-serif; color: var(--paper); letter-spacing: 0.3px;
  }
  .service-list .bullet {
    width: 17px; height: 17px; border: 2px solid var(--paper);
    margin-right: 13px; flex: none;
  }
  .brand-square {
    position: absolute; left: 520px; top: 70px; width: 100px; height: 104px;
    background: var(--navy);
  }
  .brand-divider {
    position: absolute; left: 641px; top: 56px; width: 2px; height: 136px;
    background: var(--steel);
  }
  .brand-name {
    position: absolute; left: 660px; top: 72px; width: 470px;
    font: 700 58px/1 "Titillium Web", sans-serif; color: var(--navy);
    letter-spacing: 1px; white-space: nowrap;
  }
  .brand-tagline {
    position: absolute; left: 662px; top: 135px;
    font: 28px/1 "Questrial", sans-serif; color: var(--steel);
    letter-spacing: 8.6px; white-space: nowrap;
  }
</style>
</head>
<body>
<main class="sign">
  <svg class="sign-shapes" viewBox="0 0 1327 663" preserveAspectRatio="none" aria-hidden="true">
    <rect width="1327" height="663" fill="var(--ink)"/>
    <polygon points="404,0 1327,0 1327,255 539,255" fill="var(--paper)"/>
    <polygon points="0,0 404,0 667,495 577,663 0,663" fill="var(--navy)"/>
    <polygon points="577,663 667,495 756,663" fill="var(--mist)"/>
  </svg>

  <h1 class="hiring-title">NOW<br>HIRING</h1>

  <ul class="role-list">
    <li><svg class="tick" viewBox="0 0 30 30"><path d="M24 9 A12 12 0 1 1 20 4.5" fill="none" stroke="#fff" stroke-width="2.5"/><path d="M8 15 l6 6 L28 4" fill="none" stroke="#fff" stroke-width="3" stroke-linecap="round"/></svg>Superintendents</li>
    <li><svg class="tick" viewBox="0 0 30 30"><path d="M24 9 A12 12 0 1 1 20 4.5" fill="none" stroke="#fff" stroke-width="2.5"/><path d="M8 15 l6 6 L28 4" fill="none" stroke="#fff" stroke-width="3" stroke-linecap="round"/></svg>Project Managers</li>
    <li><svg class="tick" viewBox="0 0 30 30"><path d="M24 9 A12 12 0 1 1 20 4.5" fill="none" stroke="#fff" stroke-width="2.5"/><path d="M8 15 l6 6 L28 4" fill="none" stroke="#fff" stroke-width="3" stroke-linecap="round"/></svg>Pipe Foremen</li>
    <li><svg class="tick" viewBox="0 0 30 30"><path d="M24 9 A12 12 0 1 1 20 4.5" fill="none" stroke="#fff" stroke-width="2.5"/><path d="M8 15 l6 6 L28 4" fill="none" stroke="#fff" stroke-width="3" stroke-linecap="round"/></svg>Pipe Layers</li>
    <li><svg class="tick" viewBox="0 0 30 30"><path d="M24 9 A12 12 0 1 1 20 4.5" fill="none" stroke="#fff" stroke-width="2.5"/><path d="M8 15 l6 6 L28 4" fill="none" stroke="#fff" stroke-width="3" stroke-linecap="round"/></svg>Equipment Operators</li>
  </ul>

  <div class="brand-square"></div>
  <div class="brand-divider"></div>
  <p class="brand-name">HARLAN RIDGE</p>
  <p class="brand-tagline">CIVIL CONSTRUCTION</p>

  <ul class="service-list">
    <li><span class="bullet"></span>Civil Construction Services</li>
    <li><span class="bullet"></span>Land Clearing</li>
    <li><span class="bullet"></span>Excavation</li>
    <li><span class="bullet"></span>Underground Utilities</li>
    <li><span class="bullet"></span>Environmental Maintenance</li>
  </ul>
</main>
</body>
</html>
```